Business cards to launch an education platform

Hi,
I am looking at having new business cards designed.
I am a startup, developing a web platform for schools and university, the education world. It's an online assessment system.
I would like a card that looks classy, and that is using the colors and the font of my logo.

I have attached:
1) my logo
2) A business card that I have designed quickly so you can have all the information required in the card, but I really don't like it.
3) The font that I am using (Lato Regular) to design my web platform
4) Some screenshots of my web platform so you can have a look at the style that I have.

Target Market(s)

Major market: Education system: Schools and university
Minor markets: Business in general

Industry/Entity Type

Business

Contact Information for Business Card

Lydia Marsh
Director

M: 0437 681 902
E: lydia.marsh@copperLeafSystems.com.au

Requirements
Must have
• The colors of my logo

```html
<!DOCTYPE html>
<html lang="en">
<head>
<meta charset="utf-8">
<title>Copper Leaf Systems – Business Cards</title>
<link href="https://fonts.googleapis.com/css2?family=Lato:wght@400;700&display=swap" rel="stylesheet">
<style>
  :root {
    --backdrop: #2e2a28;
    --paper: #fbfbfb;
    --brand-blue: #1f63a8;
    --brand-blue-deep: #0f4f94;
    --brand-blue-light: #3a8fd6;
    --ink: #1d1d1d;
    --white: #ffffff;
  }
  * { box-sizing: border-box; margin: 0; padding: 0; }
  html, body {
    width: 1200px;
    height: 844px;
    overflow: hidden;
    background: var(--backdrop);
    font-family: "Lato", sans-serif;
  }
  .canvas {
    position: relative;
    width: 1200px;
    height: 844px;
  }
  .card {
    position: absolute;
    top: 264px;
    width: 520px;
    height: 316px;
    border-radius: 4px;
    overflow: hidden;
    box-shadow: 0 10px 28px rgba(0, 0, 0, 0.45);
  }

  /* Front */
  .card--front {
    left: 60px;
    background: var(--paper);
  }
  .brand {
    position: absolute;
    top: 62px;
    left: 150px;
    display: flex;
    align-items: center;
    gap: 14px;
  }
  .brand__square {
    width: 50px;
    height: 50px;
    background: var(--brand-blue);
  }
  .brand__name {
    font-size: 27px;
    font-weight: 400;
    letter-spacing: 1.5px;
    color: var(--brand-blue);
    line-height: 1.1;
  }
  .contact {
    position: absolute;
    left: 34px;
    bottom: 30px;
    color: var(--ink);
  }
  .contact__name {
    font-size: 19px;
    font-weight: 700;
    color: var(--brand-blue);
  }
  .contact__role {
    font-size: 14px;
    margin-bottom: 16px;
  }
  .contact__line {
    display: flex;
    align-items: center;
    gap: 8px;
    font-size: 14px;
    line-height: 1.7;
  }
  .contact__icon {
    width: 12px;
    height: 12px;
    fill: var(--brand-blue);
    flex: none;
  }

  /* Back */
  .card--back {
    left: 620px;
    background: radial-gradient(circle at 62% 38%, var(--brand-blue-light) 0%, var(--brand-blue) 38%, var(--brand-blue-deep) 100%);
  }
  .back-brand {
    position: absolute;
    right: 46px;
    top: 132px;
    font-size: 30px;
    font-weight: 400;
    letter-spacing: 2px;
    color: var(--white);
  }
</style>
</head>
<body>
  <main class="canvas">
    <section class="card card--front" aria-label="Business card front">
      <div class="brand">
        <span class="brand__square"></span>
        <span class="brand__name">Copper Leaf Systems</span>
      </div>
      <div class="contact">
        <p class="contact__name">Lydia Marsh</p>
        <p class="contact__role">Director</p>
        <p class="contact__line">
          <svg class="contact__icon" viewBox="0 0 24 24" aria-hidden="true"><path d="M6.6 10.8a15.1 15.1 0 0 0 6.6 6.6l2.2-2.2c.3-.3.7-.4 1-.2 1.1.4 2.3.6 3.6.6.6 0 1 .4 1 1V20c0 .6-.4 1-1 1C10.6 21 3 13.4 3 4c0-.6.4-1 1-1h3.5c.6 0 1 .4 1 1 0 1.3.2 2.5.6 3.6.1.3 0 .7-.2 1z"/></svg>
          0437 681 902
        </p>
        <p class="contact__line">
          <svg class="contact__icon" viewBox="0 0 24 24" aria-hidden="true"><path d="M2 5h20v14H2z M2 5l10 8 10-8" fill="currentColor"/><path d="M2 6l10 8 10-8" fill="none" stroke="#fbfbfb" stroke-width="1.6"/></svg>
          lydia.marsh@copperLeafSystems.com.au
        </p>
      </div>
    </section>

    <section class="card card--back" aria-label="Business card back">
      <p class="back-brand">Copper Leaf Systems</p>
    </section>
  </main>
</body>
</html>
```